Prom Night 2011 theme

I am looking for a theme to best represent a high school "prom night". Design will be printed on slightly smaller than business card size paper. This is a clean sheet design, nothing is out of bounds so use you imagination. Target audience is high school age students. Design should have text "Prom Night 2011" incorporated into it. Colors are limitless.

```html
<!DOCTYPE html>
<html lang="en">
<head>
<meta charset="utf-8">
<title>Prom Night 2011 – Card Concepts</title>
<link href="https://fonts.googleapis.com/css2?family=Archivo:wght@400;700;800&display=swap" rel="stylesheet">
<style>
  :root {
    --page: #ffffff;
    --board-top: #ffffff;
    --board-bottom: #d9d9db;
    --board-line: #a9a9ab;
    --ink-grey: #58585a;
    --ink-white: #ffffff;
    --purple: #a24c9f;
    --purple-light: #c68bc4;
    --night: #000000;
    --shadow: rgba(0, 0, 0, 0.35);
  }
  * { box-sizing: border-box; margin: 0; padding: 0; }
  html, body {
    width: 1200px; height: 972px; overflow: hidden;
    background: var(--page);
    font-family: "Archivo", "Helvetica Neue", Arial, sans-serif;
  }
  .board {
    position: absolute; left: 107px; top: 77px;
    width: 989px; height: 803px;
    border: 1px solid var(--board-line);
    border-radius: 27px;
    background: linear-gradient(to bottom, var(--board-top) 0%, var(--board-top) 45%, var(--board-bottom) 100%);
  }
  .card {
    position: absolute; width: 457px; height: 211px; overflow: hidden;
    box-shadow: 3px 4px 8px var(--shadow);
  }
  .card--petals { left: 147px; top: 112px; background: #fff; }
  .card--burst  { left: 539px; top: 365px; background: var(--purple); }
  .card--stars  { left: 224px; top: 621px; background: var(--night); }

  .title {
    position: absolute; display: grid;
    grid-template-columns: auto auto; align-items: end;
    font-weight: 800; line-height: 0.8; z-index: 2;
    white-space: nowrap;
  }
  .title__prom {
    grid-row: 1 / 3; writing-mode: vertical-rl; transform: rotate(180deg);
    font-size: 20px; letter-spacing: -0.5px; margin-right: 1px;
  }
  .title__night { font-size: 56px; letter-spacing: -2.5px; }
  .title__year  { font-size: 18px; letter-spacing: -0.3px; font-weight: 700; line-height: 1; }
  .title--grey  { color: var(--ink-grey); }
  .title--white { color: var(--ink-white); }

  .card--petals .title { left: 16px; top: 18px; }
  .card--burst  .title { right: 20px; bottom: 22px; }
  .card--stars  .title { left: 14px; top: 18px; }

  .art { position: absolute; }
  .art--petals {
    left: 0; bottom: 0; width: 100%; height: 140px;
    background:
      linear-gradient(to bottom, #ffffff 0%, rgba(255,255,255,0.6) 35%, rgba(255,255,255,0) 75%),
      linear-gradient(to right, #3fb6e0 0%, #9fd45a 25%, #f5d24a 45%, #f3a35e 65%, #e59a88 80%, #b49ad2 100%);
  }
  .art--wash {
    inset: 0;
    background: linear-gradient(100deg, var(--purple) 0%, var(--purple) 45%, var(--purple-light) 100%);
  }
  .art--bloom {
    left: 0; top: 0; width: 300px; height: 200px;
    background:
      radial-gradient(ellipse at 30% 25%, #f7c94a 0%, #f08a2a 22%, #e5579f 45%, rgba(162,76,159,0) 72%);
  }
  .art--rainbow {
    left: 0; top: 59px; width: 100%; height: 152px;
    background:
      linear-gradient(to bottom, rgba(0,0,0,0) 0%, #e4262a 30%, #f47b20 40%, #ffd400 50%, #4cb847 60%, #2e8fd1 70%, #7a3f98 80%, rgba(0,0,0,0) 100%);
    opacity: 0.9;
  }
  .tagline {
    position: absolute; left: 270px; top: 178px; z-index: 2;
    color: var(--ink-white); font-size: 14px; font-weight: 400; letter-spacing: -0.2px;
  }
</style>
</head>
<body>
  <div class="board"></div>

  <section class="card card--petals">
    <div class="art art--petals" role="img" aria-label="Soft rainbow flame-like petals rising along the bottom"></div>
    <h1 class="title title--grey">
      <span class="title__prom">Prom</span>
      <span class="title__night">Night</span>
      <span class="title__year">2011</span>
    </h1>
    <p class="tagline">Let the party begin...</p>
  </section>

  <section class="card card--burst">
    <div class="art art--wash" role="img" aria-label="Purple background with light rays spreading from the top left"></div>
    <div class="art art--bloom" role="img" aria-label="Colourful swirling flowers, stars and ornaments bursting from the top left corner"></div>
    <h2 class="title title--white">
      <span class="title__prom">Prom</span>
      <span class="title__night">Night</span>
      <span class="title__year">2011</span>
    </h2>
  </section>

  <section class="card card--stars">
    <div class="art art--rainbow" role="img" aria-label="Flowing rainbow wave with swirls and scattered white stars on black"></div>
    <h2 class="title title--white">
      <span class="title__prom">Prom</span>
      <span class="title__night">Night</span>
      <span class="title__year">2011</span>
    </h2>
  </section>
</body>
</html>
```